Implant Denture Brochure

I would like to make a brochure to advertise implant dentures. This is for my dental clinic. I would like there to be some info about different implant denture options and advertise general cost. I like to use blue as a color and white. I may want to add or remove info based on the layout. Images of dentures with implants but no real photos just drawings or educational images. Real images of people smiling with dentures.

Upper
1. Implants for Upper Denture Implant Supported Removable $10,000 - $12,000 ( Includes fee for extraction of remaining upper teeth, in office sedation fees, Implant placement and necessary surgery of at least 4 implants, Does not include denture)
2. Upper Denture Implant Supported Fixed Bridge (Zirconia) $25,000 (Includes fee for extraction of all upper teeth, in office sedation fee, Implant placement and necessary surgery of at least 4 implants, includes temporary denture, and final denture)

Lower
1. Implants for Removable Lower Denture Implant Retained $5,000 - $7,000 (Includes fee for extraction of remaining lower teeth, in office sedation fees, Implant placement and necessary surgery of at least 2 implants, Does not include denture)

2. Implants for Removable Lower Denture Implant Supported $10,000 - $12,000 (Includes fee for extraction of remaining lower teeth, in office sedation fees, Implant placement and necessary surgery of at least 4 implants, Does not include denture)

3. Lower Denture Implant Supported Fixed Bridge (Zirconia) $25,000 (Includes fee for extraction of all upper teeth, in office sedation fee, Implant placement and necessary surgery of at least 4 implants, includes temporary denture, and final denture)

Copper Brook Dental
#7 - 518 Larkspur Rd E.
Copper Brook, Alberta

```html
<!DOCTYPE html>
<html lang="en">
<head>
<meta charset="utf-8">
<title>Copper Brook Dental – Implant Denture Options</title>
<link href="https://fonts.googleapis.com/css2?family=Fira+Sans:wght@400;500;600&family=Montserrat:wght@500;600&display=swap" rel="stylesheet">
<style>
  :root{
    --page:#e9ebee;
    --navy:#2a2382;
    --blue:#1b86e6;
    --blue-text:#1a78df;
    --ink:#1b1b1f;
    --white:#ffffff;
    --photo-light:#f3f1ee;
    --photo-mid:#d9d2c8;
  }
  *{margin:0;padding:0;box-sizing:border-box}
  html,body{width:1200px;height:1200px;overflow:hidden;background:var(--page)}
  .flyer{position:absolute;left:178px;top:3px;width:843px;height:1193px;background:var(--white);overflow:hidden;font-family:"Fira Sans",sans-serif}
  .flyer-shapes{position:absolute;inset:0;width:843px;height:1193px}
  .brand{position:absolute;left:44px;top:42px;display:flex;align-items:center;gap:16px}
  .brand-dot{width:58px;height:58px;border-radius:50%;background:var(--ink)}
  .brand-name{font-family:"Fira Sans",sans-serif;font-weight:500;font-size:34px;line-height:40px;letter-spacing:2px;color:var(--ink)}
  .upper-panel{position:absolute;left:36px;top:510px;width:337px;height:562px;background:var(--blue);border-radius:3px;box-shadow:0 3px 8px rgba(20,20,80,.25);padding:56px 28px 0 28px;color:var(--white)}
  .option-title{font-weight:600;font-size:25px;line-height:30.5px}
  .upper-panel .price{color:#cfe4fa}
  .option-note{font-size:15.5px;line-height:19.6px;text-align:justify;margin-top:6px}
  .upper-panel .option + .option{margin-top:36px}
  .upper-panel .option + .option .option-note{margin-top:14px}
  .lower-list{position:absolute;left:406px;top:622px;width:404px}
  .lower-list .option-title{color:var(--blue-text);font-size:21.5px;line-height:28.5px;letter-spacing:-0.1px;white-space:nowrap}
  .lower-list .price{color:var(--navy)}
  .lower-list .option-note{color:var(--ink);font-size:14.4px;line-height:19.6px;margin-top:1px}
  .lower-list .option-retained{position:absolute;left:0;top:0;width:100%}
  .lower-list .option-supported{position:absolute;left:0;top:140px;width:100%}
  .lower-list .option-fixed{position:absolute;left:0;top:285px;width:100%}
  .contact{position:absolute;left:56px;top:1099px;right:40px;color:var(--white);font-family:"Montserrat",sans-serif;font-size:15px;line-height:19px}
  .contact-row{display:flex;align-items:flex-start;gap:6px}
  .contact-address strong{font-weight:600}
  .contact-links{display:flex;gap:28px;margin-top:11px}
  .icon{width:22px;height:22px;flex:none}
</style>
</head>
<body>
<div class="flyer">
  <svg class="flyer-shapes" viewBox="0 0 843 1193">
    <defs>
      <linearGradient id="photoTone" x1="0" y1="0" x2="1" y2="1">
        <stop offset="0" stop-color="#f3f1ee"/>
        <stop offset=".6" stop-color="#d9d2c8"/>
        <stop offset="1" stop-color="#efe9e2"/>
      </linearGradient>
    </defs>
    <rect x="0" y="0" width="843" height="620" fill="url(#photoTone)" role="img" aria-label="Photo of a smiling family of four dressed in white in a bright room"/>
    <path d="M0,1193 L0,515 C250,515 420,560 540,562 C680,566 760,500 843,498 L843,1193 Z" fill="var(--blue)"/>
    <path d="M0,468 C200,418 380,540 560,585 C610,596 650,590 680,556 C640,602 590,617 520,607 C380,588 200,502 0,522 Z" fill="var(--navy)"/>
    <path d="M0,528 C200,508 380,586 560,610 C690,626 770,572 843,562 L843,1193 L0,1193 Z" fill="var(--white)"/>
    <path d="M0,945 C100,948 250,960 374,1045 C460,1095 600,1112 843,1025 L843,1193 L0,1193 Z" fill="var(--blue)"/>
    <path d="M0,956 C110,959 255,974 374,1055 C465,1105 610,1120 843,1037 L843,1193 L0,1193 Z" fill="var(--white)"/>
    <path d="M0,962 C120,965 260,985 374,1065 C470,1115 620,1130 843,1047 L843,1193 L0,1193 Z" fill="var(--navy)"/>
  </svg>

  <div class="brand">
    <div class="brand-dot"></div>
    <div class="brand-name">COPPER BROOK<br>DENTAL</div>
  </div>

  <section class="upper-panel">
    <div class="option">
      <h2 class="option-title">IMPLANTS FOR<br>Upper Denture Implant<br>Supported Removable<br><span class="price">$10,000 - $12,000</span></h2>
      <p class="option-note">Includes fee for extraction of remaining upper teeth, in office sedation fees, Implant placement &amp; necessary surgery of at least 4 implants, Does not include denture</p>
    </div>
    <div class="option">
      <h2 class="option-title">Upper Denture Implant<br>Supported Fixed Bridge<br>(Zirconia) <span class="price">$25,000</span></h2>
      <p class="option-note">Includes fee for extraction of all upper teeth, in office sedation fee, Implant placement and necessary surgery of at least 4 implants, includes temporary denture, and final denture</p>
    </div>
  </section>

  <section class="lower-list">
    <div class="option option-retained">
      <h2 class="option-title">Implants for Removable Lower Denture<br>Implant Retained <span class="price">$5,000 - $7,000</span></h2>
      <p class="option-note">Includes fee for extraction of remaining lower teeth, in office sedation fees, Implant placement and necessary surgery of at least 2 implants, Does not include denture</p>
    </div>
    <div class="option option-supported">
      <h2 class="option-title">Implants for Removable Lower Denture<br>Implant Supported <span class="price">$10,000 - $12,000</span></h2>
      <p class="option-note">Includes fee for extraction of remaining lower teeth, in office sedation fees, Implant placement and necessary surgery of at least 4 implants, Does not include denture</p>
    </div>
    <div class="option option-fixed">
      <h2 class="option-title">Lower Denture Implant Supported<br>Fixed Bridge (Zirconia) <span class="price">$25,000</span></h2>
      <p class="option-note">Includes fee for extraction of all upper teeth, in office sedation fee, Implant placement and necessary surgery of at least 4 implants, includes temporary denture, and final denture</p>
    </div>
  </section>

  <footer class="contact">
    <div class="contact-row contact-address">
      <svg class="icon" viewBox="0 0 22 22"><circle cx="11" cy="11" r="10" fill="none" stroke="#4aa3f0" stroke-width="1.4"/><path d="M11 5.5a3.5 3.5 0 0 0-3.5 3.5c0 2.6 3.5 6.5 3.5 6.5s3.5-3.9 3.5-6.5A3.5 3.5 0 0 0 11 5.5z" fill="none" stroke="#4aa3f0" stroke-width="1.3"/><circle cx="11" cy="9" r="1.2" fill="#4aa3f0"/></svg>
      <div><strong>Copper Brook Dental</strong><br>#7 - 518 Larkspur Rd E. Copper Brook, Alberta</div>
    </div>
    <div class="contact-links">
      <div class="contact-row">
        <svg class="icon" viewBox="0 0 22 22"><circle cx="11" cy="11" r="10" fill="none" stroke="#4aa3f0" stroke-width="1.4"/><path d="M7.5 6.5l2 0 1 2.5-1.3 1c.6 1.3 1.5 2.2 2.8 2.8l1-1.3 2.5 1v2c0 .6-.5 1-1 1-4 0-7.5-3.5-7.5-7.5 0-.5.4-1 1-1z" fill="none" stroke="#4aa3f0" stroke-width="1.2"/></svg>
        <span>403-555-0148</span>
      </div>
      <div class="contact-row">
        <svg class="icon" viewBox="0 0 22 22"><circle cx="11" cy="11" r="10" fill="none" stroke="#4aa3f0" stroke-width="1.4"/><rect x="6" y="7.5" width="10" height="7" rx="1" fill="none" stroke="#4aa3f0" stroke-width="1.2"/><path d="M6.3 8l4.7 3.6L15.7 8" fill="none" stroke="#4aa3f0" stroke-width="1.2"/></svg>
        <span>copperbrookdental@gmail.com</span>
      </div>
      <div class="contact-row">
        <svg class="icon" viewBox="0 0 22 22"><circle cx="11" cy="11" r="10" fill="none" stroke="#4aa3f0" stroke-width="1.4"/><circle cx="11" cy="11" r="5" fill="none" stroke="#4aa3f0" stroke-width="1.2"/><ellipse cx="11" cy="11" rx="2.2" ry="5" fill="none" stroke="#4aa3f0" stroke-width="1.1"/><path d="M6 11h10" stroke="#4aa3f0" stroke-width="1.1"/></svg>
        <span>www.copperbrookdental.ca</span>
      </div>
    </div>
  </footer>
</div>
</body>
</html>
```